Website Design for Spatial Humanities Non-Profit: Civic Landmark Atlas

We seek a Wordpress website template for Civic Landmark Atlas (CLA) a 501(c)(3) non-profit in the emergent field of spatial humanities dedicated to digitally preserving global historic and cultural sites. A unique collaboration between individuals in diverse disciplines (academia, technology, arts, and social entrepreneurship), CLA melds age-old scholarship with 21st Century technology to assert the importance of physical location to the understanding of history. This actualized focus allows for a more comprehensive, interactive, and “living” reconstruction of the past than previously thought possible.
CLA, through its own initiatives as well as those of others to whom it provides services, has created a prototype for digital preservation applicable to every country, culture, and subject matter. The organization is
• Pioneering new technology and multimedia techniques for documenting historic and cultural sites;
• Leading international field expeditions to geo-locate and digitize sites, as well as record eyewitness testimony; and
• Transforming research data into dynamically new educational applications.
The template should have a distinctive homepage, themed pages (about, news, projects, opportunities), and no blog elements (e.g., comment section). Admin friendliness is a plus.
We have posted separately for a logo design, which will perhaps feature a scattering of pixels horizontally that gradually cohere to form a globe (featuring "CLA") in the center. To participate in that contest see: http://gigs.pixelvaultwork.com/gig.aspx?id=48213
Non-Profit

```html
<!DOCTYPE html>
<html lang="en">
<head>
<meta charset="utf-8">
<title>Civic Landmark Atlas</title>
<link href="https://fonts.googleapis.com/css2?family=Source+Sans+3:wght@400;600;700&family=PT+Sans+Narrow&display=swap" rel="stylesheet">
<style>
:root{
  --sky-top:#abdef2;
  --sky-bottom:#2ba6de;
  --ink:#656a6e;
  --ink-on-sky:#5d7888;
  --accent:#1b8fd0;
  --navy-top:#03071a;
  --navy-bottom:#16296a;
  --rule:#1c2a38;
  --footer:#0f5c80;
  --footer-edge:#0a4763;
  --footer-link:#d3e9f3;
  --ribbon:#3fa9dc;
  --icon:#2f6f9a;
  --placeholder:#85857f;
  --page-edge:#c9c9c9;
}
*{margin:0;padding:0;box-sizing:border-box}
html,body{width:1020px;height:1200px;overflow:hidden;background:#fff}
body{position:relative;font-family:"Source Sans 3",sans-serif;color:var(--ink)}
.page-frame{position:absolute;left:50px;top:0;width:906px;height:1061px;border-left:1px solid var(--page-edge);border-right:1px solid var(--page-edge)}
.brand{position:absolute;left:70px;top:14px;display:flex;align-items:center;gap:10px}
.brand-mark{width:48px;height:48px;background:var(--ribbon);border-radius:6px}
.brand-name{font-size:30px;font-weight:400;color:#7c7f82;letter-spacing:1px}
.hero{position:absolute;left:0;top:67px;width:1020px;height:309px;background:linear-gradient(var(--sky-top) 0%,var(--sky-top) 40%,var(--sky-bottom) 100%)}
.main-nav{position:absolute;top:104px;font-family:"PT Sans Narrow",sans-serif;font-size:17px;color:#1d3442}
.main-nav a,.footer-nav a{position:absolute;white-space:nowrap;text-decoration:none;color:inherit}
.nav-marker{position:absolute;left:86px;top:98px;width:0;height:0;border-left:6px solid transparent;border-right:6px solid transparent;border-top:7px solid #111}
.nav-rule{position:absolute;left:58px;top:128px;width:884px;height:2px;background:var(--rule)}
.search-field{position:absolute;background:#fff;border:1px solid #6a8da0}
.search-icon{position:absolute}
.ribbon{position:absolute}
.slider{position:absolute;left:85px;top:166px;width:383px;height:184px;background:linear-gradient(var(--navy-top),var(--navy-bottom))}
.slider-title{position:absolute;right:18px;top:8px;color:#fff;font-weight:700;font-size:15px;letter-spacing:.6px}
.slider-bar{position:absolute;left:82px;top:307px;width:388px;height:23px;background:rgba(190,200,215,.6)}
.slider-dots{position:absolute;left:360px;top:318px}
.intro{position:absolute;left:506px;top:165px;width:401px;font-size:12.6px;line-height:15px;color:var(--ink-on-sky)}
.intro p{margin-bottom:15px;text-align:justify}
.intro .on-blue{color:#fff}
.column{position:absolute;top:415px;width:400px;font-size:12.6px;line-height:15.2px;text-align:justify}
.column h2,.feature h2{color:var(--accent);font-weight:600;font-size:13px;line-height:15.5px;margin-bottom:15px}
.column p{margin-bottom:15px}
.dash{position:absolute;left:58px;width:884px;border-top:1px dashed #333}
.feature{position:absolute;left:72px;width:630px;font-size:12.4px;line-height:15.2px}
.feature h2{text-transform:uppercase;margin-bottom:13px}
.feature p{margin-bottom:14px;text-align:justify}
.feature p.clip{text-align:left;white-space:nowrap;overflow:hidden}
.feature-image{position:absolute;left:719px;width:179px;height:130px;background:var(--placeholder);color:#fff;font-size:29px;font-weight:600;display:flex;align-items:center;justify-content:center}
.footer{position:absolute;left:0;top:1061px;width:1020px;height:139px;background:var(--footer);border-top:3px solid var(--footer-edge)}
.footer-nav{position:absolute;top:1075px;font-family:"PT Sans Narrow",sans-serif;font-size:15px;letter-spacing:.9px;color:var(--footer-link)}
.footer-search{position:absolute;left:679px;top:1076px;width:190px;height:18px;background:#a3d6ee}
.copyright{position:absolute;top:1186px;left:0;width:956px;text-align:center;font-size:7px;color:#08314a}
</style>
</head>
<body>
<div class="page-frame"></div>

<header>
  <div class="brand"><span class="brand-mark"></span><span class="brand-name">CLA</span></div>
</header>

<section class="hero"></section>

<nav class="main-nav">
  <a style="left:76px;top:0">Home</a>
  <a style="left:128px;top:0">About</a>
  <a style="left:181px;top:0">News</a>
  <a style="left:230px;top:0">Projects</a>
  <a style="left:295px;top:0">Opportunities</a>
  <a style="left:395px;top:0">Contact</a>
</nav>
<div class="nav-marker"></div>
<div class="nav-rule"></div>

<div class="search-field" style="left:666px;top:106px;width:192px;height:19px"></div>
<svg class="search-icon" style="left:860px;top:106px" width="18" height="18" viewBox="0 0 18 18"><circle cx="7" cy="7" r="5" fill="none" stroke="#1b6ea0" stroke-width="2"/><line x1="11" y1="11" x2="16" y2="16" stroke="#1b6ea0" stroke-width="2.5"/></svg>

<svg class="ribbon" style="left:898px;top:0" width="44" height="103" viewBox="0 0 44 103">
  <path d="M0 0H44V103L22 88L0 103Z" fill="var(--ribbon)"/>
  <path d="M4 0V94L22 82L40 94V0" fill="none" stroke="#bfe4f5" stroke-width="1" stroke-dasharray="2 2"/>
  <rect x="12" y="9" width="20" height="20" rx="3" fill="var(--icon)"/>
  <rect x="12" y="33" width="20" height="20" rx="3" fill="var(--icon)"/>
  <rect x="12" y="57" width="20" height="20" rx="3" fill="var(--icon)"/>
</svg>

<div class="slider" role="img" aria-label="Gallery slideshow of documented heritage sites">
  <div class="slider-title">Civic Landmark Atlas INC Gallery</div>
</div>
<div class="slider-bar"></div>
<svg class="slider-dots" width="80" height="10" viewBox="0 0 80 10">
  <path d="M0 5L4 2V8Z" fill="#2aa5dc"/>
  <circle cx="14" cy="5" r="3" fill="#e8eef5"/><circle cx="26" cy="5" r="3" fill="#2aa5dc"/>
  <circle cx="38" cy="5" r="3" fill="#e8eef5"/><circle cx="50" cy="5" r="3" fill="#e8eef5"/>
  <circle cx="62" cy="5" r="3" fill="#e8eef5"/>
  <path d="M78 5L74 2V8Z" fill="#2aa5dc"/>
</svg>

<div class="intro">
  <p>Lorem Ipsum is simply dummy text of the printing and typesetting industry.</p>
  <p>Lorem Ipsum has been the industry's standard dummy text ever since the 1500s, when an unknown printer took a galley of type and scrambled it to make a type specimen book. It has survived not only five centuries, but also the leap into electronic typesetting, remaining essentially unchanged. It was popularised in the 1960s with the release of Typeleaf sheets containing Lorem Ipsum passages, and more recently with desktop publishing software like Quire PageSetter including versions of Lorem Ipsum.</p>
  <p class="on-blue">t has survived not only five centuries, but also the leap into electronic type-setting, remaining essentially unchanged. It was popularised in the 1960s</p>
</div>

<article class="column" style="left:68px">
  <h2>Lorem Ipsum is simply dummy text of the printing and typesetting industry.</h2>
  <p>Lorem Ipsum has been the industry's standard dummy text ever since the 1500s, when an unknown printer took a galley of type and scrambled it to make a type specimen book. It has survived not only five centuries, but also the leap into electronic typesetting, remaining essentially unchanged. It was popularised in the 1960s with the release of Typeleaf sheets containing Lorem Ipsum passages, and more recently with desktop publishing software like Quire PageSetter including versions of Lorem Ipsum.</p>
  <p>t has survived not only five centuries, but also the leap into electronic type-</p>
</article>
<article class="column" style="left:511px">
  <h2>Lorem Ipsum is simply dummy text of the printing and typesetting industry.</h2>
  <p>Lorem Ipsum has been the industry's standard dummy text ever since the 1500s, when an unknown printer took a galley of type and scrambled it to make a type specimen book. It has survived not only five centuries, but also the leap into electronic typesetting, remaining essentially unchanged. It was popularised in the 1960s with the release of Typeleaf sheets containing Lorem Ipsum passages, and more recently with desktop publishing software like Quire PageSetter including versions of Lorem Ipsum.</p>
  <p>t has survived not only five centuries, but also the leap into electronic type-</p>
</article>

<div class="dash" style="top:640px"></div>

<article class="feature" style="top:689px">
  <h2>Lorem Ipsum is simply dummy text of the printing and typesetting industry.</h2>
  <p>Lorem Ipsum has been the industry's standard dummy text ever since the 1500s, when an unknown printer took a galley of type and scrambled it to make a type specimen book. It has survived not only five centuries, but also the leap into elec-tronic typesetting, remaining essentially unchanged. It was popularised in the 1960s with the release of Typeleaf sheets containing Lorem Ipsum passages, and more recently with desktop publishing software like Quire PageSetter including versions of Lorem Ipsum.</p>
  <p class="clip">t has survived not only five centuries, but also the leap into electronic typesetting, remaining essentially unchanged. It</p>
</article>
<div class="feature-image" style="top:695px" role="img" aria-label="Project photograph">image</div>

<div class="dash" style="top:850px"></div>

<article class="feature" style="top:873px">
  <h2>Lorem Ipsum is simply dummy text of the printing and typesetting industry.</h2>
  <p>Lorem Ipsum has been the industry's standard dummy text ever since the 1500s, when an unknown printer took a galley of type and scrambled it to make a type specimen book. It has survived not only five centuries, but also the leap into elec-tronic typesetting, remaining essentially unchanged. It was popularised in the 1960s with the release of Typeleaf sheets containing Lorem Ipsum passages, and more recently with desktop publishing software like Quire PageSetter including versions of Lorem Ipsum.</p>
  <p class="clip">t has survived not only five centuries, but also the leap into electronic typesetting, remaining essentially unchanged. It</p>
</article>
<div class="feature-image" style="top:880px" role="img" aria-label="Project photograph">image</div>

<footer class="footer"></footer>
<nav class="footer-nav">
  <a style="left:84px;top:0">Home</a>
  <a style="left:137px;top:0">About</a>
  <a style="left:190px;top:0">News</a>
  <a style="left:239px;top:0">Projects</a>
  <a style="left:305px;top:0">Opportunities</a>
  <a style="left:404px;top:0">Contact</a>
</nav>
<div class="footer-search"></div>
<svg class="search-icon" style="left:872px;top:1075px" width="18" height="18" viewBox="0 0 18 18"><circle cx="7" cy="7" r="5" fill="none" stroke="#d3e9f3" stroke-width="2"/><line x1="11" y1="11" x2="16" y2="16" stroke="#d3e9f3" stroke-width="2.5"/></svg>
<svg class="ribbon" style="left:901px;top:1061px" width="42" height="102" viewBox="0 0 42 102">
  <path d="M0 0H42V102L21 88L0 102Z" fill="var(--ribbon)"/>
  <path d="M4 0V93L21 82L38 93V0" fill="none" stroke="#bfe4f5" stroke-width="1" stroke-dasharray="2 2"/>
  <rect x="11" y="9" width="20" height="20" rx="3" fill="var(--icon)"/>
  <rect x="11" y="33" width="20" height="20" rx="3" fill="var(--icon)"/>
  <rect x="11" y="57" width="20" height="20" rx="3" fill="var(--icon)"/>
</svg>
<div class="copyright">CLA copyright 2012</div>
</body>
</html>
```